Objective: Create a visually stunning and compelling PDF brochure that showcases The Orvelle Peak Lodge as the ultimate luxury hunting destination in Kyrgyzstan, specializing in Marco Polo and Ibex hunts. The PDF should evoke a sense of exclusivity, adventure, and the breathtaking beauty of the Tian Shan mountains, ultimately driving bookings.
Target Audience: High-net-worth individuals, discerning hunters seeking exceptional experiences, adventure travelers, and those interested in unique and luxurious wilderness experiences.
Overall Tone & Style: Sophisticated, elegant, and aspirational. Think high-end travel magazines combined with a touch of rugged adventure. Avoid anything that feels generic or overly commercial. The design should reflect the unparalleled nature of the lodge and the hunts offered. (I'm attaching a reference PDF that i like), as well as another instructions file. Drive link for photos: https://files.brankolu.net/share/folders/7KRM42PTbWq0vnzeHJ5sudYA913_c8LxE?mode=view
Another Link: https://files.brankolu.net/share/u/0/folders/5TWEpk-m8rzaqoLc2BnvXwiyeSKdfuGtm

```html
<!DOCTYPE html>
<html lang="en">
<head>
<meta charset="utf-8">
<title>The Orvelle Peak Lodge — Brochure</title>
<link href="https://fonts.googleapis.com/css2?family=Gloock&family=Lato:wght@400;700&family=Raleway:wght@300;400&display=swap" rel="stylesheet">
<style>
:root{
  --red:#be1e2d;
  --ink:#222;
  --paper:#fff;
  --backdrop:#8e8e8e;
}
*{box-sizing:border-box;margin:0;padding:0}
html,body{width:1200px;height:4987px;overflow:hidden}
body{background:var(--backdrop);font-family:"Lato",sans-serif;color:var(--ink);position:relative}
.page{position:absolute;left:372px;width:457px;height:646px;background:var(--paper);overflow:hidden}
.abs{position:absolute}
.serif{font-family:"Gloock",serif;font-weight:400}
.photo{position:absolute}
.pill{position:absolute;background:var(--red);color:#fff;font-size:13px;font-weight:700;border-radius:12px;padding:2px 18px;letter-spacing:.3px;white-space:nowrap}
.pill.centered{left:50%;transform:translateX(-50%)}
.pill.light{background:#fff;color:var(--red)}
.body-text{position:absolute;font-size:7.2px;line-height:1.35;text-align:justify}
.brand{position:absolute;font-family:"Lato",sans-serif;font-weight:700;font-size:11px;color:var(--ink);display:flex;align-items:center;gap:5px;white-space:nowrap}
.brand .dot{width:9px;height:9px;border-radius:50%;background:var(--red)}
.section-title{position:absolute;left:35px;color:var(--red);font-size:29px;letter-spacing:1px;padding-bottom:4px;border-bottom:1.5px solid var(--red);white-space:nowrap}
.sub-label{position:absolute;left:53px;color:var(--red);font-size:11px;text-decoration:underline}
.item{position:absolute;left:53px;font-size:9px;white-space:nowrap}
.circle{position:absolute;width:144px;height:144px;border-radius:50%;border:3px solid var(--red);transform:translate(-50%,-50%)}
.red-base{position:absolute;left:-60px;width:577px;background:var(--red);border-radius:50% 50% 0 0 / 22% 22% 0 0}
.white{color:#fff}

/* photo tones */
.tone-cover{background:
  radial-gradient(ellipse 60% 30% at 30% 18%,#e6e4e1 0%,rgba(230,228,225,0) 100%),
  radial-gradient(ellipse 40% 45% at 55% 50%,#5e4636 0%,rgba(94,70,54,0) 100%),
  radial-gradient(ellipse 55% 40% at 85% 40%,#7b5c44 0%,rgba(123,92,68,0) 100%),
  linear-gradient(180deg,#c9c6c1 0%,#a99580 22%,#8f7058 50%,#9a7b60 75%,#6e5443 100%)}
.tone-trophy{background:
  radial-gradient(ellipse 30% 20% at 50% 30%,#5a4f48 0%,rgba(90,79,72,0) 100%),
  radial-gradient(ellipse 35% 30% at 60% 62%,#c7ab8a 0%,rgba(199,171,138,0) 100%),
  radial-gradient(ellipse 35% 25% at 15% 68%,#e4e8ec 0%,rgba(228,232,236,0) 100%),
  radial-gradient(ellipse 30% 20% at 85% 75%,#4a4440 0%,rgba(74,68,64,0) 100%),
  linear-gradient(180deg,#9b7a5e 0%,#7f6150 35%,#8d7866 60%,#b7b6b4 85%,#3f3a36 100%)}
.tone-valley{background:
  radial-gradient(ellipse 40% 12% at 55% 72%,#8e8a88 0%,rgba(142,138,136,0) 100%),
  linear-gradient(180deg,#e6e7e8 0%,#d2d4d5 55%,#8f8781 70%,#7d6a5a 80%,#8c6a46 100%)}
.tone-camp{background:
  radial-gradient(ellipse 30% 25% at 45% 30%,#6a5a4c 0%,rgba(106,90,76,0) 100%),
  radial-gradient(ellipse 25% 25% at 55% 70%,#d8d3cc 0%,rgba(216,211,204,0) 100%),
  radial-gradient(ellipse 30% 25% at 85% 60%,#3e3530 0%,rgba(62,53,48,0) 100%),
  linear-gradient(180deg,#e0e1e2 0%,#b6ada3 30%,#6f5d4e 55%,#5a4a3d 75%,#a1834f 100%)}
.tone-lounge{background:
  radial-gradient(ellipse 45% 18% at 55% 78%,#2fa39a 0%,rgba(47,163,154,0) 100%),
  radial-gradient(ellipse 20% 30% at 85% 55%,#3a2414 0%,rgba(58,36,20,0) 100%),
  radial-gradient(ellipse 35% 20% at 45% 55%,#d79b5c 0%,rgba(215,155,92,0) 100%),
  linear-gradient(180deg,#4a2e1a 0%,#8a5a30 40%,#b37c45 62%,#7b5030 100%)}
</style>
</head>
<body>

<section class="page cover" style="top:103px">
  <h1 class="abs serif" style="top:28px;width:100%;text-align:center;color:var(--red);font-size:27px">The Orvelle Peak Lodge</h1>
  <div class="brand" style="left:68px;top:114px"><span class="dot"></span>Trailmark</div>
  <div class="brand" style="left:290px;top:114px"><span class="dot"></span>Stonecrest Studio</div>
  <div class="photo tone-cover" role="img" aria-label="Hunter on horseback riding up a rocky mountain valley"
       style="left:0;top:162px;width:457px;height:484px;border-top:3px solid var(--red);border-radius:50% 50% 0 0/24% 24% 0 0"></div>
  <div class="pill" style="left:24px;top:606px;font-size:15px;padding:3px 14px">Kyrgyzstan 2025</div>
</section>

<section class="page intro" style="top:788px">
  <h2 class="abs serif" style="left:44px;top:30px;font-size:29px;letter-spacing:1px;white-space:nowrap">A HUNTER'S PARADISE:</h2>
  <p class="abs" style="left:44px;top:64px;font-family:'Raleway',sans-serif;font-weight:300;color:var(--red);font-size:21px">Where Luxury Roams Free</p>
  <p class="body-text" style="left:44px;top:98px;width:370px">Renowned as one of the best mountain hunting lodges in the world, this Kyrgyzstan camp offers adventure and luxury in the majestic Tian Shan Mountains. Hunt Marco Polo sheep and Ibex across rugged terrain, then relax in unparalleled comfort. Unwind in this secluded oasis, surrounded by breathtaking panoramas of the Kyrgyz landscape. This is where the adventure of the hunt seamlessly blends with the comforts of an unparalleled wilderness retreat.</p>
  <div class="photo tone-trophy" role="img" aria-label="Hunter kneeling behind a large curled-horn Marco Polo ram in snowy mountains"
       style="left:-35px;top:186px;width:527px;height:620px;border-radius:50%"></div>
</section>

<section class="page details" style="top:1478px">
  <div class="photo tone-valley" role="img" aria-label="Wide mountain valley under an overcast sky"
       style="left:-40px;top:-210px;width:537px;height:445px;border-radius:50%"></div>
  <h2 class="abs serif" style="top:33px;width:100%;text-align:center;font-size:29px;letter-spacing:1px">HUNT DETAILS</h2>
  <div class="pill centered" style="top:240px">HIGHLIGHTS</div>
  <p class="body-text" style="left:22px;top:262px;width:413px">Experience an unforgettable hunting adventure in Kyrgyzstan's majestic Tian Shan Mountains. Pursue the elusive Marco Polo sheep and Siberian Ibex, hunting on horseback alongside seasoned local guides. Sharpen your long-range shooting skills, as accuracy at 400-500 meters may be required. The breathtaking scenery, from towering peaks to vast valleys, provides a stunning backdrop. This unique combination of challenging hunts and unparalleled landscapes creates a truly once-in-a-lifetime experience.</p>
  <div class="pill centered" style="top:326px">PROPERTY FACTS</div>
  <p class="body-text" style="left:22px;top:348px;width:413px">Nestled deep within the majestic Tian Shan mountains, this hunting camp, a unique endeavor by the Kyrgyz government, offers an unparalleled wilderness experience. While the eight luxurious rooms each provide private bathrooms and unexpected amenities like reliable WiFi, the communal spaces truly capture the grandeur of the surroundings. The lounge area, with its striking floor-to-ceiling windows, frames breathtaking panoramic views of the rugged landscape, blending modern comforts and untouched wilderness like no other.</p>
  <div class="pill centered" style="top:421px">GETTING THERE</div>
  <p class="abs" style="top:444px;width:100%;text-align:center;color:var(--red);font-size:11px">Recommended Route</p>
  <p class="body-text" style="left:22px;top:460px;width:413px">International flights typically arrive at Manas International Airport (FRU) in Bishkek, Kyrgyzstan, often with layovers in Istanbul or Dubai. Upon arrival, our team will assist with firearms clearance. For guests arriving late, overnight accommodations in Bishkek can be arranged. From Bishkek, hunters have two options to reach the hunting area in the mountains: a 10-hour scenic drive or a 2.5-hour helicopter flight.</p>
  <div class="abs" role="img" aria-label="Route map from Bishkek to the hunting area"
       style="left:23px;top:516px;width:413px;height:110px;border:2.5px solid var(--red);border-radius:16px;background:linear-gradient(115deg,#eeeeef 0%,#dcdcdd 35%,#cbb697 60%,#c6a57a 100%)">
    <svg class="abs" style="left:210px;top:30px" width="22" height="30" viewBox="0 0 22 30"><path d="M11 0C5 0 0 5 0 11c0 8 11 19 11 19s11-11 11-19C22 5 17 0 11 0z" fill="var(--red)"/><circle cx="11" cy="11" r="4" fill="#fff"/></svg>
  </div>
</section>

<section class="page pricing" style="top:2167px">
  <h2 class="section-title serif" style="top:18px">DATES &amp; PRICING</h2>
  <div class="pill" style="left:35px;top:73px">SEASON DATES</div>
  <p class="abs" style="left:200px;top:76px;font-size:11px">August 15th 2025 – November 30th 2025</p>
  <div class="pill" style="left:35px;top:116px;padding:2px 28px">INCLUSIONS</div>
  <p class="sub-label" style="top:146px">GUIDED HUNT</p>
  <p class="item" style="top:176px">7-day guided horseback hunt for Marco Polo Argali, Ibex or Both</p>
  <p class="item" style="top:192px">Exclusive access to some of the finest hunting areas in Kyrgyzstan</p>
  <p class="item" style="top:209px">Trophy Skinning and field preparation</p>
  <p class="sub-label" style="top:238px">FOOD &amp; DRINK</p>
  <p class="item" style="top:269px">Chef-prepared breakfast, packed lunch and dinner</p>
  <p class="item" style="top:285px">A selection of non-alcoholic beverages</p>
  <p class="sub-label" style="top:312px">TRAVEL &amp; LOGISTICS</p>
  <p class="item" style="top:343px">Pre-arrival custom planning with the Trailmark Team</p>
  <p class="item" style="top:359px">Round trip, fixed-time airport transfers to Bishkek</p>
  <div class="red-base" style="top:392px;height:300px"></div>
  <div class="pill light" style="left:35px;top:426px;padding:2px 70px 2px 20px">PRICING</div>
  <p class="item white" style="top:459px">MARCO POLO AND IBEX COMBO - $39,500 (min. 2 hunters)</p>
  <p class="item white" style="top:478px">MARCO POLO ARGALI - $32,500 (min. 2 hunters)</p>
  <p class="item white" style="top:497px">MID-ASIAN IBEX - $10,500 (Min. 2 hunters)</p>
  <div class="pill light" style="left:35px;top:540px">POPULAR ADD ONS</div>
  <p class="item white" style="top:575px">WOLF (Opportunistic) $2,500</p>
  <p class="item white" style="top:592px">Extra Ibex $5,500</p>
</section>

<section class="page adventures" style="top:2864px">
  <h2 class="section-title serif" style="top:20px">THE ADVENTURES</h2>
  <div class="circle" role="img" aria-label="Riders on horseback crossing a ridge" style="left:99px;top:149px;background:radial-gradient(ellipse 50% 25% at 50% 55%,#5c4a3c 0%,rgba(92,74,60,0) 100%),linear-gradient(180deg,#d8d9da 0%,#b9b4ad 45%,#8c7461 100%)"></div>
  <div class="circle" role="img" aria-label="Hunting party with horses in the mountains" style="left:348px;top:149px;background:radial-gradient(ellipse 40% 40% at 50% 60%,#3f3630 0%,rgba(63,54,48,0) 100%),linear-gradient(180deg,#b9b9b8 0%,#8a8580 50%,#5d5247 100%)"></div>
  <p class="abs" style="left:39px;top:248px;font-size:13.5px;line-height:1.45">A Horseback Ride You'll Never Forget.<br>Challenging Hunts For Prized Game.</p>
  <div class="circle" role="img" aria-label="Hunter glassing across a mountain slope" style="left:348px;top:325px;background:radial-gradient(ellipse 45% 35% at 30% 70%,#6e5542 0%,rgba(110,85,66,0) 100%),linear-gradient(180deg,#d0d1d3 0%,#a8978a 45%,#8b6e57 100%)"></div>
  <div class="photo tone-camp" role="img" aria-label="Hunting camp with saddled horses and guides beneath mountain peaks"
       style="left:-60px;top:363px;width:577px;height:340px;border-top:3px solid var(--red);border-radius:50% 50% 0 0/24% 24% 0 0"></div>
  <p class="abs white" style="left:16px;top:476px;font-size:13.5px;line-height:1.45">A Stunning Camp To Revitalize Your Spirit.<br>This Is The Hunt Of A Lifetime.</p>
</section>

<section class="page lodge" style="top:3560px">
  <div class="photo tone-lounge" role="img" aria-label="Lodge lounge with timber walls and a pool table"
       style="left:-60px;top:-300px;width:577px;height:575px;border-bottom:3px solid var(--red);border-radius:0 0 50% 50%/0 0 20% 20%"></div>
  <h2 class="abs serif white" style="left:40px;top:26px;font-size:30px;letter-spacing:1px">THE LODGE</h2>
  <div class="circle" role="img" aria-label="Trophy room with mounted horns" style="left:108px;top:281px;background:radial-gradient(ellipse 40% 30% at 50% 40%,#d09a5e 0%,rgba(208,154,94,0) 100%),linear-gradient(180deg,#6b4427,#b07a45)"></div>
  <div class="circle" role="img" aria-label="Wood-panelled lounge with trophy mounts" style="left:344px;top:281px;background:radial-gradient(ellipse 40% 30% at 40% 45%,#e0aa6a 0%,rgba(224,170,106,0) 100%),linear-gradient(180deg,#7a4d2c,#c28e57)"></div>
  <p class="abs" style="left:23px;top:372px;width:410px;font-size:10.5px;line-height:1.45">Beyond The Reach Of Ordinary Travel Lies A Hidden World Of Spectacular Beauty And Unrivaled Hunting.</p>
  <p class="abs" style="left:23px;top:408px;width:410px;font-size:10.5px;line-height:1.45">Our Kyrgyzstan Experience Is Crafted For The Discerning Sportsman, Offering Access To Pristine Wilderness And Luxurious Accommodations. This Is Hunting Elevated To An Art Form.</p>
  <div class="circle" role="img" aria-label="Lodge exterior entrance at dusk" style="left:108px;top:534px;background:radial-gradient(ellipse 35% 30% at 50% 55%,#e0a457 0%,rgba(224,164,87,0) 100%),linear-gradient(180deg,#2e2119,#6b4a2e)"></div>
  <div class="circle" role="img" aria-label="Warm timber hallway inside the lodge" style="left:344px;top:534px;background:radial-gradient(ellipse 20% 35% at 50% 50%,#f2c384 0%,rgba(242,195,132,0) 100%),linear-gradient(180deg,#5a3520,#c58a4c)"></div>
</section>

<section class="page back" style="top:4247px">
  <div class="brand" style="left:50%;transform:translateX(-50%);top:100px;font-size:16px"><span class="dot"></span>Trailmark</div>
  <div class="brand" style="left:50%;transform:translateX(-50%);top:283px;font-size:16px"><span class="dot"></span>Stonecrest Studio</div>
  <div class="red-base" style="top:358px;height:340px"></div>
  <p class="abs white" style="top:420px;width:100%;text-align:center;font-size:9px">+961 555 0192</p>
  <p class="abs white" style="top:596px;width:100%;text-align:center;font-size:8px">www.trailmark-hunts.com</p>
  <p class="abs white" style="top:612px;width:100%;text-align:center;font-size:8px">hello@trailmark-hunts.com</p>
</section>

</body>
</html>
```